Web Design for ROLV Air conditioning company

Hello,

I am calling on you for the modernization of the company's website
https://clarovent-services-techniques.fr/

The new one must include the new logo with the new graphic charter (color, style ...)

I'm looking for a simple design (less is more), a font written without Serif, the logo that brings a touch of color and modernity.

(maintenance and installation company for air conditioning and ventilation systems)
COLORS: in line with the logo

CHAPTER:

# PRESENTATION
# SERVICES
AIR CONDITIONING (ice cube icon)
HEATING (flame icon)
AIR TREATMENT (icon fan)
# ACHIEVEMENTS

# CONTACT
CONTACT FORM
GOOGLE MAPS

Target Market(s)

Showcase site for our customers

Coding

Coded - Design and coding required

Number of Pages Required

4 page

Font styles to use
Sans Serif

Colors
33b8a4
33a6d7
3176b5
ffffff

Requirements
Must have
• Clear and fluid navigation
a visual identity of the page with the logo
Should not have
• Overloaded.

```html
<!DOCTYPE html>
<html lang="en">
<head>
<meta charset="utf-8">
<title>ROLV – Air Conditioning &amp; Ventilation Services</title>
<link href="https://fonts.googleapis.com/css2?family=Josefin+Sans:wght@600;700&family=Lato:wght@400;700&display=swap" rel="stylesheet">
<style>
:root{
  --navy:#1f3f63;
  --band:#244b73;
  --blue:#3176b5;
  --sky:#33a6d7;
  --teal:#33b8a4;
  --text:#4f5d6b;
  --muted:#6f7c89;
  --white:#ffffff;
  --band-text:#e4edf5;
  --field:#f6f8fa;
  --line:#e0e6ec;
}
*{margin:0;padding:0;box-sizing:border-box}
html,body{width:1200px;height:3958px;overflow:hidden;background:var(--white)}
body{position:relative;font-family:"Lato",Arial,sans-serif;color:var(--text)}
.abs{position:absolute}
.heading{font-family:"Josefin Sans",Arial,sans-serif;font-weight:700;letter-spacing:.5px}
.band{position:absolute;left:0;width:1200px}
/* nav */
.brand{left:80px;top:42px;display:flex;align-items:flex-end;gap:14px}
.brand-name{font-family:"Josefin Sans",sans-serif;font-weight:700;font-size:44px;color:var(--teal);line-height:1}
.brand-tag{font-size:12.5px;font-weight:700;color:var(--blue);margin-bottom:2px}
.nav{left:742px;top:37px;display:flex;font-size:13.5px;color:var(--muted);letter-spacing:.5px}
.nav a{color:inherit;text-decoration:none;padding:7px 11px;height:29px;line-height:16px;margin-right:6px}
.nav a.active{color:var(--teal);border:1px solid var(--teal)}
/* hero */
.hero-title{left:80px;top:183px;font-size:40px;line-height:50px;color:var(--navy)}
.accent{color:var(--teal)}.accent-blue{color:var(--sky)}
.hero-text{left:80px;top:300px;width:400px;font-size:15px;line-height:28px;color:var(--navy)}
.ph{position:absolute}
/* welcome */
.welcome-title{left:610px;top:764px;font-size:38px;color:var(--white)}
.welcome-text{left:610px;top:832px;width:505px;font-size:15px;line-height:27px;color:var(--band-text)}
.welcome-text p+p{margin-top:16px}
.btn-light{left:607px;top:1071px;width:240px;height:52px;border-radius:26px;background:var(--white);color:var(--navy);font-size:18px;display:flex;align-items:center;justify-content:center}
/* sections */
.section-title{left:0;width:1200px;text-align:center;font-size:40px}
.section-text{left:305px;width:590px;text-align:center;font-size:15px;line-height:28px}
.service{width:320px;text-align:center}
.diamond{width:74px;height:74px;border:1px solid var(--line);transform:rotate(45deg);background:var(--white);margin:0 auto}
.service-icon{position:absolute;left:50%;top:15px;transform:translateX(-50%)}
.service h3{margin-top:40px;font-size:21px;color:var(--navy)}
.service p{margin-top:20px;font-size:15px;line-height:28px;color:var(--text)}
/* team */
.card{width:323px;height:374px;background:var(--white);text-align:center}
.portrait{position:absolute;left:50%;top:-66px;width:132px;height:132px;margin-left:-66px;transform:rotate(45deg);background:linear-gradient(135deg,#c6ccd3,#6f7a86)}
.card h4{position:absolute;left:0;right:0;top:130px;font-size:21px;color:var(--navy)}
.card .role{position:absolute;left:0;right:0;top:170px;font-size:17px;color:var(--navy)}
.card .bio{position:absolute;left:18px;right:18px;top:212px;font-size:14.5px;line-height:27px;color:var(--muted)}
/* form */
.label{font-size:12px;color:var(--muted)}
.field{background:var(--field);border:1px solid var(--line)}
.select-text{font-size:12.5px;color:#94a0ac;padding:14px 14px}
.btn-dark{left:516px;top:3752px;width:168px;height:52px;background:var(--blue);color:var(--white);font-size:20px;display:flex;align-items:center;justify-content:center}
.rule{left:77px;top:3886px;width:1045px;height:1px;background:var(--line)}
.copy{left:0;width:1200px;top:3913px;text-align:center;font-size:12.5px;color:var(--muted)}
</style>
</head>
<body>

<svg class="band" style="top:456px" width="1200" height="855" viewBox="0 0 1200 855" aria-hidden="true">
  <polygon points="0,0 1200,128 1200,855 0,732" fill="var(--band)"/>
</svg>
<svg class="band" style="top:2243px" width="1200" height="1060" viewBox="0 0 1200 1060" aria-hidden="true">
  <polygon points="0,0 1200,123 1200,1060 0,934" fill="var(--band)"/>
</svg>

<header>
  <div class="abs brand">
    <span class="brand-name">ROLV</span>
    <span class="brand-tag">CLAROVENT SERVICES TECHNIQUES</span>
  </div>
  <nav class="abs nav">
    <a class="active">HOME</a><a>SERVICES</a><a>ABOUT</a><a>TEAM</a><a>CONTACT</a>
  </nav>
</header>

<section class="hero">
  <h1 class="abs heading hero-title"><span class="accent">ON-DEMAND</span><br>FACILITY <span class="accent">SERVICES</span></h1>
  <p class="abs hero-text">Lorem ipsum dolor sit amet, consectetur adipiscing elit, sed do eiusm tempor incididunt ut labore et dolor.</p>
  <div class="ph" style="left:525px;top:131px;width:604px;height:465px;border-radius:24px;background:linear-gradient(135deg,#f3f6f9,#d6dee6)" role="img" aria-label="Split air conditioner indoor and outdoor units"></div>
</section>

<section class="welcome">
  <div class="ph" style="left:37px;top:768px;width:455px;height:523px;border-radius:6px;background:linear-gradient(135deg,#d5dce3,#96a3b0)" role="img" aria-label="Heating and air treatment equipment"></div>
  <h2 class="abs heading welcome-title">WELCOME TO VENTIVA</h2>
  <div class="abs welcome-text">
    <p>Lorem ipsum dolor sit amet, consectetur adipiscing elit, sed do eiusm tempor incididunt ut labore et dolore magna aliqua. Ut enim ad minim veniam, quis nostrud exercitation ullamco laboris nisi ut aliquip ex ea commodo consequat. Duis aute irure dolor in reprehenderit.</p>
    <p>Ut enim ad minim veniam, quis nostrud exercitation ullamco laborisni ut aliquip ex ea commodo consequat. Duis aute irure dolor in rhenderit in voluptate velit esse cillum dolore eu fugiat nulla pariatur.</p>
  </div>
  <a class="abs heading btn-light">REQUEST SERVICE</a>
</section>

<section class="services">
  <h2 class="abs heading section-title" style="top:1368px;color:var(--navy)">OUR <span class="accent">SERVICES</span></h2>
  <p class="abs section-text" style="top:1436px">Lorem ipsum dolor sit amet, consectetur adipiscing elit, sed do eiusmod tempor incididunt ut labore et dolore magna aliqua. Ut enim ad minim veniam.</p>

  <div class="ph" style="left:0;top:1828px;width:800px;height:431px;background:radial-gradient(ellipse at 35% 40%,#c7d3de 0%,#e6ecf1 45%,rgba(255,255,255,0) 75%)" role="img" aria-label="Technician servicing a ceiling air conditioning unit"></div>

  <div class="abs service" style="left:78px;top:1549px">
    <div style="position:relative"><div class="diamond"></div>
      <svg class="service-icon" width="44" height="44" viewBox="0 0 44 44" aria-hidden="true"><polygon points="22,5 38,13 22,21 6,13" fill="var(--sky)"/><polygon points="6,13 22,21 22,39 6,31" fill="var(--blue)"/><polygon points="38,13 22,21 22,39 38,31" fill="var(--teal)"/></svg>
    </div>
    <h3 class="heading">AIR CONDITIONING</h3>
    <p>Lorem ipsum dolor sit amet, consectetur adipiscing elit, sed do eiusmod temp.</p>
  </div>
  <div class="abs service" style="left:439px;top:1622px">
    <div style="position:relative"><div class="diamond"></div>
      <svg class="service-icon" width="44" height="44" viewBox="0 0 44 44" aria-hidden="true"><path d="M22 4 C24 12 33 17 33 27 A11 11 0 0 1 11 27 C11 20 16 17 17 11 C20 15 20 19 22 21 C24 16 22 9 22 4 Z" fill="var(--blue)"/><path d="M22 24 C24 28 27 29 27 33 A5 5 0 0 1 17 33 C17 30 20 28 22 24 Z" fill="var(--sky)"/></svg>
    </div>
    <h3 class="heading">HEATING</h3>
    <p>Lorem ipsum dolor sit amet, consectetur adipiscing elit, sed do eiusmod temp.</p>
  </div>
  <div class="abs service" style="left:800px;top:1695px">
    <div style="position:relative"><div class="diamond"></div>
      <svg class="service-icon" width="44" height="44" viewBox="0 0 44 44" aria-hidden="true"><g fill="var(--teal)"><ellipse cx="22" cy="12" rx="5" ry="9"/><ellipse cx="22" cy="12" rx="5" ry="9" transform="rotate(120 22 22)"/><ellipse cx="22" cy="12" rx="5" ry="9" transform="rotate(240 22 22)"/></g><circle cx="22" cy="22" r="4" fill="var(--blue)"/></svg>
    </div>
    <h3 class="heading">AIR TREATMENT</h3>
    <p>Lorem ipsum dolor sit amet, consectetur adipiscing elit, sed do eiusmod temp.</p>
  </div>
</section>

<section class="team">
  <h2 class="abs heading section-title" style="top:2395px;color:var(--white)">OUR TEAM</h2>
  <p class="abs section-text" style="top:2463px;color:var(--band-text)">Lorem ipsum dolor sit amet, consectetur adipiscing elit, sed do eiusmod tempor incididunt ut labore et dolore magna aliqua. Ut enim ad minim veniam.</p>

  <article class="abs card" style="left:77px;top:2673px">
    <div class="portrait" role="img" aria-label="Portrait of team member"></div>
    <h4 class="heading">NAME SURNAME</h4>
    <p class="role">Lorem ipsum dolor sitamet.</p>
    <p class="bio">Lorem ipsum dolor sit amet, conse adipiscing elit, sed do eiusmod tempor incididunt ut labore et dolore magna aliqua. Ut enim ad minim veniam.</p>
  </article>
  <article class="abs card" style="left:438px;top:2736px">
    <div class="portrait" role="img" aria-label="Portrait of team member" style="background:linear-gradient(135deg,#b9b0a6,#5d5650)"></div>
    <h4 class="heading">NAME SURNAME</h4>
    <p class="role">Lorem ipsum dolor sitamet.</p>
    <p class="bio">Lorem ipsum dolor sit amet, conse adipiscing elit, sed do eiusmod tempor incididunt ut labore et dolore magna aliqua. Ut enim ad minim veniam.</p>
  </article>
  <article class="abs card" style="left:799px;top:2798px">
    <div class="portrait" role="img" aria-label="Portrait of team member" style="background:linear-gradient(135deg,#7e9a6a,#3e5434)"></div>
    <h4 class="heading">NAME SURNAME</h4>
    <p class="role">Lorem ipsum dolor sitamet.</p>
    <p class="bio">Lorem ipsum dolor sit amet, conse adipiscing elit, sed do eiusmod tempor incididunt ut labore et dolore magna aliqua. Ut enim ad minim veniam.</p>
  </article>
</section>

<section class="quote">
  <h2 class="abs heading section-title" style="top:3322px;color:var(--navy)">GET A <span class="accent">FREE</span> <span class="accent-blue">QUOTE</span></h2>
  <span class="abs label" style="left:252px;top:3402px">Name*</span>
  <span class="abs label" style="left:617px;top:3402px">Email*</span>
  <div class="abs field" style="left:252px;top:3426px;width:333px;height:47px"></div>
  <div class="abs field" style="left:616px;top:3426px;width:334px;height:47px"></div>
  <span class="abs label" style="left:252px;top:3500px">Phone*</span>
  <span class="abs label" style="left:617px;top:3500px">Choose Service*</span>
  <div class="abs field" style="left:252px;top:3526px;width:333px;height:46px"></div>
  <div class="abs field select-text" style="left:616px;top:3526px;width:334px;height:46px">-- Select Service --</div>
  <svg class="abs" style="left:914px;top:3543px" width="18" height="12" viewBox="0 0 18 12" aria-hidden="true"><polyline points="3,3 9,9 15,3" fill="none" stroke="var(--navy)" stroke-width="2"/></svg>
  <span class="abs label" style="left:252px;top:3598px">Message*</span>
  <div class="abs field" style="left:252px;top:3625px;width:698px;height:103px"></div>
  <a class="abs heading btn-dark">SUBMIT</a>
</section>

<footer>
  <div class="abs rule"></div>
  <p class="abs copy">©Ventiva - 2019. All Rights Reserved.</p>
</footer>

</body>
</html>
```